【 概要 】 自動車学校で販促活動に使用するチラシを作りたいと考えています。 短期で免許取得を希望の方に向けたチラシデザインを募集します。 【 依頼内容 】 ・サイズ:B5 両面 ・ページ数:1ページ ・素材の用意(画像・文章等):最初はフリー素材で作っていただき、確定次第データをお渡しいたします。 ・デザイン内容:以下に添付してある.pptxを参考にしてください。 裏面は魅力を並べているだけですが、可愛らしく雰囲気のあるデザインがあれば嬉しいです。 ・納品形式:AI【アウトラインなし、アウトラインあり】でお願いします。 【 デザインイメージ 】 ・ターゲット層:高校3年生の保護者様 35歳〜50歳 ・雰囲気:温かみのあるデザイン ・参考デザイン: 広沢自動車学校HP/https://nashino-ds.com 【 契約金額(税抜) 】5万円 ※契約金額(税込)からシステム利用料を差し引いた金額が、ワーカーさまの受取金額となります その他ご質問等ありましたら、気軽にお問い合わせください。 たくさんのご応募をお待ちしております! |
| https://nashino-ds.com/ | ||
どの提案も素敵でとても迷いましたが、デザインが弊社のイメージに近い方を採用させていただきました。
皆様、ご提案ありがとうございました。提案全てが素晴らしく一名のみの採用で迷い、選考に時間を割いてしまって申し訳ありません。またの機会があれば、ぜひよろしくお願いいたします。

```html
<!DOCTYPE html>
<html lang="ja">
<head>
<meta charset="utf-8">
<title>梨野自動車学校 7つの魅力</title>
<link href="https://fonts.googleapis.com/css2?family=M+PLUS+Rounded+1c:wght@500;700;800;900&family=Noto+Sans+JP:wght@500;700;900&display=swap" rel="stylesheet">
<style>
:root{
  --bg:#f9d9df;
  --bg-dot:#fbe6ea;
  --red:#e0343f;
  --pink:#ec6d86;
  --ink:#3a3030;
  --white:#ffffff;
  --c1:#4aa3d8;
  --c2:#7cc45a;
  --c3:#9b7cc0;
  --c4:#f2a03a;
  --c5:#52b8a0;
  --c6:#f08a3e;
  --c7:#e8607c;
  --foot:#ffffff;
}
*{box-sizing:border-box;margin:0;padding:0}
html,body{width:851px;height:1200px;overflow:hidden}
body{
  background:var(--bg);
  background-image:radial-gradient(var(--bg-dot) 2px,transparent 2.5px);
  background-size:22px 22px;
  font-family:"M PLUS Rounded 1c","Noto Sans JP",sans-serif;
  color:var(--ink);
  position:relative;
}
.header{position:absolute;left:0;top:0;width:851px;height:280px}
.school-name{
  position:absolute;left:120px;top:21px;width:611px;height:85px;
  background:var(--white);border:4px solid var(--pink);border-radius:14px;
  display:flex;align-items:center;justify-content:center;
  font-weight:900;font-size:56px;color:var(--red);letter-spacing:4px;
}
.headline{
  position:absolute;left:0;top:120px;width:851px;text-align:center;
  font-weight:900;font-size:74px;color:var(--red);letter-spacing:4px;
}
.headline .num{
  display:inline-block;width:98px;height:104px;line-height:104px;
  background:var(--red);color:var(--white);border-radius:16px;
  font-size:88px;margin-right:8px;vertical-align:middle;
}
.headline .rest{vertical-align:middle}
.seven-points{position:absolute;left:615px;top:150px;font-style:italic;color:var(--pink);font-size:20px;font-weight:700;line-height:1}
.mascot{position:absolute;border-radius:50%}
.mascot-left{left:40px;top:100px;width:150px;height:160px;background:radial-gradient(circle at 50% 40%,#f6c244,#e49a2c)}
.mascot-right{left:690px;top:40px;width:140px;height:180px;background:radial-gradient(circle at 50% 40%,#d7a77a,#b37f55)}

.card{
  position:absolute;background:var(--white);border-radius:10px;
  box-shadow:0 3px 0 rgba(0,0,0,.07);overflow:hidden;
}
.card::before{content:"";position:absolute;left:0;top:0;right:0;height:8px;background:var(--accent)}
.badge{
  position:absolute;left:10px;top:14px;width:44px;height:44px;border-radius:8px;
  background:var(--accent);color:var(--white);font-weight:900;font-size:32px;
  display:flex;align-items:center;justify-content:center;
}
.c1{--accent:var(--c1);left:40px;top:293px;width:372px;height:160px}
.c2{--accent:var(--c2);left:434px;top:293px;width:377px;height:160px}
.c3{--accent:var(--c3);left:40px;top:487px;width:372px;height:165px}
.c4{--accent:var(--c4);left:434px;top:487px;width:377px;height:165px}
.c5{--accent:var(--c5);left:40px;top:692px;width:239px;height:306px}
.c6{--accent:var(--c6);left:296px;top:692px;width:250px;height:306px}
.c7{--accent:var(--c7);left:563px;top:692px;width:248px;height:306px}

.zero{position:absolute;left:0;right:0;top:18px;display:flex;align-items:center;justify-content:center;gap:16px}
.zero .label{font-size:30px;font-weight:800}
.zero .big{font-family:"Noto Sans JP",sans-serif;font-size:92px;font-weight:900;line-height:1}
.c1 .sub{position:absolute;left:0;right:0;bottom:14px;text-align:center;font-weight:800;font-size:18px}
.c1 .sub b{color:var(--red);font-size:23px}

.pickup{position:absolute;left:40px;right:0;top:20px;text-align:center}
.pickup .lead{font-size:30px;font-weight:800}
.pickup .big{font-family:"Noto Sans JP",sans-serif;font-size:70px;font-weight:900;line-height:1.1}
.pickup .unit{font-size:26px;font-weight:800}

.c3 .text{position:absolute;left:16px;top:64px;width:184px;font-size:14px;font-weight:700;line-height:1.45}
.c3 .text .em{color:var(--red);font-size:19px;font-weight:900}
.c3 .photo{position:absolute;right:14px;top:38px;width:150px;height:104px;border-radius:6px;background:linear-gradient(#c9ccd4,#8e95a3)}

.c4 .text{position:absolute;left:66px;top:20px;right:14px;font-size:14px;font-weight:700;line-height:1.5}
.c4 .award{display:block;margin-top:6px;font-size:25px;font-weight:900;line-height:1.3;border-left:4px solid var(--ink);padding-left:8px}

.card-title{position:absolute;left:60px;top:18px;right:6px;font-size:20px;font-weight:900;line-height:1.35;letter-spacing:-1px}
.c5 .photo,.c6 .photo{position:absolute;left:10px;right:10px;top:90px;bottom:10px;border-radius:6px}
.c5 .photo{background:linear-gradient(#2e3f6a,#d58a4a)}
.c6 .photo{background:linear-gradient(#f6efe6,#e3c6b0)}
.c6 .bubble{position:absolute;left:24px;top:102px;background:var(--white);border:2px solid var(--pink);border-radius:14px;padding:3px 10px;font-size:13px;font-weight:800;color:var(--pink);z-index:1}
.c7 .list{position:absolute;left:14px;top:94px;right:10px;list-style:none;font-size:15px;font-weight:800;line-height:1.6}
.c7 .list li{padding-left:1em;text-indent:-1em;margin-bottom:4px}
.c7 .list li::before{content:"・";color:var(--red)}
.c7 .note{position:absolute;left:14px;right:12px;bottom:14px;font-size:12px;font-weight:700;line-height:1.5}

.footer{position:absolute;left:0;bottom:0;width:851px;height:175px;background:var(--foot);display:flex;align-items:center;padding:0 24px;gap:20px}
.brand{display:flex;align-items:center;gap:8px;font-weight:900;color:var(--red)}
.brand .mark{width:22px;height:22px;border-radius:50%;background:var(--red)}
.brand .name{font-size:20px;line-height:1.15}
.brand .name small{display:block;font-size:12px}
.stamp{width:90px;height:90px;border-radius:50%;background:var(--pink);color:var(--white);font-size:12px;font-weight:800;display:flex;align-items:center;justify-content:center;text-align:center;line-height:1.35;flex:none}
.contact{flex:1}
.contact .hours{font-size:14px;font-weight:700}
.contact .tel{display:flex;align-items:center;gap:8px;font-family:"Noto Sans JP",sans-serif;font-size:44px;font-weight:900;line-height:1.15;color:var(--red)}
.contact .url{font-size:17px;font-weight:700}
.apply{width:110px;font-size:13px;font-weight:800;text-align:center;background:var(--pink);color:var(--white);border-radius:8px;padding:10px 4px;flex:none}
</style>
</head>
<body>
<header class="header">
  <div class="mascot mascot-left" role="img" aria-label="ライオンのマスコットキャラクター"></div>
  <div class="mascot mascot-right" role="img" aria-label="うさぎのマスコットキャラクター"></div>
  <h1 class="school-name">梨野自動車学校</h1>
  <p class="headline"><span class="num">7</span><span class="rest">つの魅力</span></p>
  <span class="seven-points">seven<br>points</span>
</header>

<section class="card c1">
  <span class="badge">1</span>
  <div class="zero"><span class="label">喫煙者</span><span class="big">0</span></div>
  <p class="sub">女性スタッフ数<b>県下トップクラス</b></p>
</section>

<section class="card c2">
  <span class="badge">2</span>
  <div class="pickup">
    <div class="lead">無料送迎</div>
    <div><span class="big">500</span><span class="unit">箇所対応!</span></div>
  </div>
</section>

<section class="card c3">
  <span class="badge">3</span>
  <p class="text">梨野のYouTuberがお届けする<span class="em">教習所チャンネル</span>で予習復習もバッチリ!</p>
  <div class="photo" role="img" aria-label="教習所チャンネルの動画画面"></div>
</section>

<section class="card c4">
  <span class="badge">4</span>
  <p class="text">消費者志向経営企業として、<span class="award">「内閣府<br>特命担当大臣表彰」を受賞!</span></p>
</section>

<section class="card c5">
  <span class="badge">5</span>
  <h2 class="card-title">美しい施設、<br>温かなサービス</h2>
  <div class="photo" role="img" aria-label="夕景の校舎の写真"></div>
</section>

<section class="card c6">
  <span class="badge">6</span>
  <h2 class="card-title">友達と一緒に<br>教習を受けられる!</h2>
  <span class="bubble">楽しく免許取得♪</span>
  <div class="photo" role="img" aria-label="笑顔の教習生二人の写真"></div>
</section>

<section class="card c7">
  <span class="badge">7</span>
  <h2 class="card-title">しっかりとした<br>コロナ対策</h2>
  <ul class="list">
    <li>マスクや手袋の着用</li>
    <li>検温・体調申告や換気の実施</li>
    <li>飛沫防止シートの設置</li>
  </ul>
  <p class="note">など他にも職員・施設・講習車内の感染防止対策を行っております。</p>
</section>

<footer class="footer">
  <div class="brand"><span class="mark"></span><span class="name">梨野自動車学校<small>NASHINO DRIVING SCHOOL</small></span></div>
  <div class="stamp">送迎バスで<br>近くから<br>乗れます!</div>
  <div class="contact">
    <p class="hours">お問い合わせ受付時間 9:00〜19:00</p>
    <p class="tel"><svg width="36" height="36" viewBox="0 0 24 24" aria-hidden="true"><path fill="#e0343f" d="M6.6 10.8a15.1 15.1 0 0 0 6.6 6.6l2.2-2.2c.3-.3.7-.4 1-.2 1.1.4 2.3.6 3.6.6.6 0 1 .4 1 1V20c0 .6-.4 1-1 1A17 17 0 0 1 3 4c0-.6.4-1 1-1h3.5c.6 0 1 .4 1 1 0 1.3.2 2.5.6 3.6.1.3 0 .7-.2 1z"/></svg>0120-000-481</p>
    <p class="url">https://nashino-ds.com</p>
  </div>
  <div class="apply">スマホから<br>お申し込み</div>
</footer>
</body>
</html>
```